Non-Fiction Book Cover Series Concepts

I need front cover concepts for a non-fiction business book series. Just concepts at this stage to show to backers (full cover designs later).

The books are for leaders and business owners. A mature, sophisticated market, AND, bold and innovative.

The series needs to be extensible - the concepts need to be able to work across at least 40 books. I am happy with a colour theme, or contrasts, or icon theme, there is no limitation to the imagination.

The books need to look like they belong to a series and to also stand alone.

I prefer simple and bold.

Imagine the Heron business series (https://www.heronbooks-example.co.uk/series/lbs/heron-leaders-masters-series.html) - but I hate these designs (the colours don't work for me).

The imprint is ThoughtfulHorizon.example - the logo mark for the imprint is attached.

The books will be printed and ebooks - the printed version will be 5 inches by 8 inches form factor. They will be printed with a matt cover.

IF YOU WANT A BOOK TITLE TO TRY, use this:

Steady Momentum: Apply the R.A.F. Model to Nurture, Unlock and Keep Talent

Thank you for your interest!

Target Market(s)

Business owners, leaders, entrepreneurs

Industry/Entity Type

Leadership

Font styles to use
Serif
Sans Serif

Requirements
Must have
• Extensible - the concept can work for many books and ALL books look part of the series
Nice to have
• I prefer simple, icons rather than photos
Should not have
• No photographic designs - icon, drawing

```html
<!DOCTYPE html>
<html lang="en">
<head>
<meta charset="utf-8">
<title>Steady Momentum – Book Cover Concept</title>
<link rel="stylesheet" href="https://fonts.googleapis.com/css2?family=Montserrat:wght@400;700;800&display=swap">
<style>
  :root {
    --page-bg: #ffffff;
    --cover-navy: #1b1b4a;
    --beam-orange: #f7941d;
    --beam-fade: #2c2548;
    --title-cream: #e8e1d3;
    --author-teal: #1fa9a8;
    --imprint-white: #f2f2f2;
  }
  html, body {
    margin: 0;
    padding: 0;
    width: 1200px;
    height: 1000px;
    overflow: hidden;
    background: var(--page-bg);
  }
  .canvas {
    position: relative;
    width: 1200px;
    height: 1000px;
  }
  .book-cover {
    position: absolute;
    left: 287px;
    top: 0;
    width: 625px;
    height: 1000px;
    background: var(--cover-navy);
  }
  .cover-art {
    position: absolute;
    inset: 0;
    width: 1200px;
    height: 1000px;
  }
  .imprint-name {
    font-family: "Montserrat", sans-serif;
    font-weight: 400;
    font-size: 11px;
    fill: var(--imprint-white);
  }
  .imprint-dot { fill: var(--imprint-white); }
  .author-name {
    font-family: "Montserrat", sans-serif;
    font-weight: 700;
    font-size: 25px;
    letter-spacing: 2.5px;
    fill: var(--author-teal);
  }
  .title-main {
    font-family: "Montserrat", sans-serif;
    font-weight: 800;
    font-size: 90px;
    fill: var(--title-cream);
  }
  .title-main.title-accent { fill: var(--beam-orange); }
  .title-vertical {
    font-family: "Montserrat", sans-serif;
    font-weight: 800;
    font-size: 50px;
    fill: var(--cover-navy);
  }
</style>
</head>
<body>
<main class="canvas">
  <div class="book-cover"></div>
  <svg class="cover-art" viewBox="0 0 1200 1000" xmlns="http://www.w3.org/2000/svg">
    <defs>
      <linearGradient id="beam-gradient" gradientUnits="userSpaceOnUse" x1="0" y1="318" x2="0" y2="1000">
        <stop offset="0" style="stop-color: var(--beam-orange)"/>
        <stop offset="0.43" style="stop-color: var(--beam-orange)"/>
        <stop offset="1" style="stop-color: var(--beam-fade)"/>
      </linearGradient>
    </defs>

    <g class="imprint">
      <circle class="imprint-dot" cx="337" cy="38" r="5"/>
      <text class="imprint-name" x="350" y="42">ThoughtfulHorizon.example</text>
    </g>

    <polygon class="light-beam" points="603,318 667,318 910,1000 352,1000" fill="url(#beam-gradient)"/>

    <text class="author-name" x="330" y="232">THE AUTHOR’S NAME</text>

    <g class="title-row">
      <text class="title-main" x="330" y="309" textLength="238" lengthAdjust="spacing">STE</text>
      <text class="title-main title-accent" x="635" y="309" text-anchor="middle">A</text>
      <text class="title-main" x="700" y="309" textLength="172" lengthAdjust="spacing">DY</text>
    </g>

    <text class="title-vertical" text-anchor="middle">
      <tspan x="635" y="392">M</tspan>
      <tspan x="635" y="452">O</tspan>
      <tspan x="635" y="512">M</tspan>
      <tspan x="635" y="572">E</tspan>
      <tspan x="635" y="632">N</tspan>
      <tspan x="635" y="692">T</tspan>
      <tspan x="635" y="752">U</tspan>
      <tspan x="635" y="812">M</tspan>
    </text>
  </svg>
</main>
</body>
</html>
```